Design a New Business Card for Our Company

We are looking for fresh, unique, and a modern business card that reflects our roots as digital marketing agency focused on SEM.

Industry/Entity Type

Marketing

Contact Information for Business Card

looking for very unique out of the box designs. clean and modern that compliments our logo

Requirements
Must have
• colors should match our logo
• Front should have name, address, email, and phone/fax of the person, phone/fax are the same number
• back should have our url

```html
<!DOCTYPE html>
<html lang="en">
<head>
<meta charset="utf-8">
<title>Brightpath Solutions – Business Card</title>
<link href="https://fonts.googleapis.com/css2?family=Arimo:ital,wght@0,400;0,700;1,400&display=swap" rel="stylesheet">
<style>
  :root{
    --page:#f1f1f1;
    --divider:#ffffff;
    --card:#ffffff;
    --blue:#1a5fa3;
    --grey:#a9b3bb;
    --logo-grey:#9c9c9c;
    --logo-blue:#4f8fd8;
    --ink:#333333;
    --rule:#b8b8b8;
  }
  *{margin:0;padding:0;box-sizing:border-box}
  html,body{width:904px;height:1200px;overflow:hidden;background:var(--page);font-family:"Arimo",Arial,sans-serif}
  .canvas{position:relative;width:904px;height:1200px}
  .half{position:absolute;left:0;width:904px;background:var(--page)}
  .half--front{top:0;height:592px}
  .half--back{top:608px;height:592px}
  .gap{position:absolute;left:0;top:592px;width:904px;height:16px;background:var(--divider)}
  .side-label{position:absolute;font-size:34px;color:#222;font-weight:400}
  .side-label--front{right:40px;top:28px}
  .side-label--back{left:32px;top:24px}

  .card{position:absolute;width:530px;height:322px;background:var(--card);transform-origin:0 0;transform:scale(.806);overflow:hidden;box-shadow:0 2px 6px rgba(0,0,0,.12)}
  .card--front{left:142px;top:137px}
  .card--back{left:334px;top:137px}
  .card-shapes{position:absolute;inset:0;width:530px;height:322px}

  .brand{position:absolute;display:flex;align-items:center;gap:8px;color:var(--logo-grey);font-weight:700;letter-spacing:-.3px;white-space:nowrap;line-height:1}
  .brand-dot{border-radius:50%;background:var(--logo-blue);flex:none}
  .card--front .brand{left:68px;top:218px;font-size:20px}
  .card--front .brand-dot{width:20px;height:20px}

  .contact{position:absolute;left:346px;top:136px;color:var(--ink);font-size:10.5px;line-height:1.38}
  .contact-name{color:var(--blue);font-weight:700;font-size:12px}
  .contact-role{font-style:italic;font-size:11.5px}
  .contact-address{margin-top:12px}
  .contact-lines{margin-top:6px}
  .contact-lines b{color:var(--blue)}
  .rule-v{position:absolute;left:330px;top:138px;width:1px;height:147px;background:var(--rule)}
  .rule-h{position:absolute;left:314px;top:167px;width:188px;height:1px;background:var(--rule)}

  .card--back .brand{left:165px;top:218px;font-size:26px;transform:rotate(-31deg);transform-origin:0 0}
  .card--back .brand-dot{width:24px;height:24px}
  .site-url{position:absolute;left:268px;top:262px;transform:rotate(-31.5deg);transform-origin:0 0;color:#ffffff;font-size:11px;white-space:nowrap}
</style>
</head>
<body>
<div class="canvas">
  <section class="half half--front">
    <div class="side-label side-label--front">Front</div>
    <article class="card card--front">
      <svg class="card-shapes" viewBox="0 0 530 322" aria-hidden="true">
        <polygon points="200,0 300,0 0,187 0,125" fill="var(--blue)"/>
        <polygon points="284,322 354,322 530,210 530,160" fill="var(--blue)"/>
        <rect x="16.5" y="16.5" width="497" height="289" fill="#fff" stroke="#d8d8d8"/>
        <polygon points="0,0 210,0 0,135" fill="var(--grey)"/>
        <polygon points="354,322 530,322 530,210" fill="var(--grey)"/>
      </svg>
      <div class="brand"><span class="brand-dot"></span>Brightpath Solutions</div>
      <div class="rule-v"></div>
      <div class="rule-h"></div>
      <div class="contact">
        <div class="contact-name">My Name</div>
        <div class="contact-role">Designation</div>
        <div class="contact-address">4870 Meadow Ridge Rd Fairview,<br>CA 90210 USA</div>
        <div class="contact-lines">
          <div><b>p</b> 555-010-4820</div>
          <div><b>f</b> 555 010 4820</div>
          <div><b>e</b> hello@brightpath.com</div>
        </div>
      </div>
    </article>
  </section>

  <div class="gap"></div>

  <section class="half half--back">
    <div class="side-label side-label--back">Back</div>
    <article class="card card--back">
      <svg class="card-shapes" viewBox="0 0 530 322" aria-hidden="true">
        <polygon points="0,0 232,0 0,143" fill="var(--grey)"/>
        <polygon points="16,16 160,16 16,105" fill="var(--blue)"/>
        <polygon points="530,75 530,322 130,322" fill="var(--grey)"/>
        <polygon points="512,130 512,305 228,305" fill="var(--blue)"/>
      </svg>
      <div class="brand"><span class="brand-dot"></span>Brightpath Solutions</div>
      <div class="site-url">www.brightpathsolutions.com</div>
    </article>
  </section>
</div>
</body>
</html>
```